Rivers of Parting - CD cover indie music

This is my 4th and final album. I am sharing my story of trials, pain and persistence that led me here, like a sound track to a short film.
I would like a design that communicates both a painful phase of life, yet tranquility and beauty found as life winds down. Can be illustrated or photograph.
On front design should have title 'Rivers of Parting' and artist name.
I will need to add credits and song list.
I am thinking a booklet will be added with lyrics and a few photos and plan to work with this artist. Thank you

Target Market(s)

Folk, easy listening, story telling

Industry/Entity Type

Indie music - independent

Font styles to use
Sans Serif
Other font styles liked:
• I like also verdana font.

Requirements
Nice to have
• a contrast of colors to emotions may work well. There is a portuguese word ‘saudade’ that expresses sadness, but longing also.
Should not have
• No bright red. Not busy. No images of people or animals.

```html
<!DOCTYPE html>
<html lang="en">
<head>
<meta charset="utf-8">
<title>Rivers of Parting — MAREN</title>
<link rel="stylesheet" href="https://fonts.googleapis.com/css2?family=Noto+Sans:wght@400;800&display=swap">
<style>
  :root {
    --sky-top: #6b50a0;
    --sky-mid: #a47cb8;
    --sky-bottom: #e6b8d6;
    --ink-light: #ffffff;
    --art-plum: #45333f;
    --art-rust: #785244;
    --art-lilac: #b89cc0;
    --art-peach: #d8ac90;
    --art-sage: #8ea068;
    --art-teal: #94b4b8;
    --art-coral: #de7470;
  }
  * { margin: 0; padding: 0; box-sizing: border-box; }
  html, body {
    width: 1200px;
    height: 1200px;
    overflow: hidden;
  }
  .cover {
    position: relative;
    width: 1200px;
    height: 1200px;
    background: linear-gradient(to bottom, var(--sky-top) 0%, var(--sky-mid) 50%, var(--sky-bottom) 100%);
    font-family: "Noto Sans", Verdana, sans-serif;
    color: var(--ink-light);
  }
  .artist-name {
    position: absolute;
    top: 22px;
    left: 130px;
    width: 953px;
    display: flex;
    justify-content: space-between;
    font-weight: 800;
    font-size: 214px;
    line-height: 1;
  }
  .artwork {
    position: absolute;
    top: 228px;
    left: 99px;
    width: 1012px;
    height: 810px;
    border-radius: 44% 44% 30% 30% / 40% 40% 22% 22%;
    background:
      radial-gradient(circle at 22% 30%, var(--art-rust) 0%, transparent 28%),
      radial-gradient(circle at 78% 30%, var(--art-sage) 0%, transparent 28%),
      radial-gradient(circle at 25% 58%, var(--art-plum) 0%, transparent 38%),
      radial-gradient(circle at 76% 58%, var(--art-peach) 0%, transparent 38%),
      radial-gradient(circle at 38% 92%, var(--sky-top) 0%, transparent 30%),
      radial-gradient(circle at 64% 92%, var(--art-teal) 0%, transparent 30%),
      radial-gradient(circle at 92% 88%, var(--art-coral) 0%, transparent 18%),
      linear-gradient(to right, var(--art-plum), var(--art-lilac) 50%, var(--art-peach));
    opacity: 0.85;
  }
  .album-title {
    position: absolute;
    top: 1030px;
    left: 0;
    width: 1200px;
    text-align: center;
    font-weight: 400;
    font-size: 110px;
    line-height: 1;
    white-space: nowrap;
  }
</style>
</head>
<body>
  <main class="cover">
    <h1 class="artist-name" aria-label="MAREN">
      <span>M</span><span>A</span><span>R</span><span>E</span><span>N</span>
    </h1>
    <div class="artwork" role="img" aria-label="Illustration of two translucent overlapping head silhouettes facing each other in muted plum, rust, peach and sage tones, with a floating stack of coloured isometric steps between them"></div>
    <h2 class="album-title">Rivers of Parting</h2>
  </main>
</body>
</html>
```